New Signage for Cafe/Deli

We are looking to draw some attention to our café/deli at the end of a corridor in a commercial office building. The graphic panel should be 4'x8' with the name "Harbor Lane Deli" somewhere in the middle. The deli mainly caters to the breakfast and lunch crowd. Attached are photos of the location (the exit sign will be moved)

Industry/Entity Type

Cafe

```html
<!DOCTYPE html>
<html lang="en">
<head>
<meta charset="utf-8">
<title>Harbor Lane Deli – Corridor Sign</title>
<link rel="stylesheet" href="https://fonts.googleapis.com/css2?family=Playball&display=swap">
<style>
  :root {
    --backdrop: #000000;
    --panel-top: #f6e2d2;
    --panel-mid: #eebc9c;
    --panel-bottom: #dc8658;
    --brand-brown: #7d4533;
    --art-light: #c98a6a;
    --art-dark: #8a4f3b;
  }
  html, body {
    margin: 0;
    padding: 0;
    width: 1200px;
    height: 824px;
    overflow: hidden;
    background: var(--backdrop);
  }
  .canvas {
    position: relative;
    width: 1200px;
    height: 824px;
  }
  .sign-panel {
    position: absolute;
    left: 100px;
    top: 162px;
    width: 1000px;
    height: 500px;
    background: linear-gradient(180deg, var(--panel-top) 0%, var(--panel-mid) 50%, var(--panel-bottom) 100%);
    overflow: hidden;
  }
  .cup-art {
    position: absolute;
    left: 0;
    top: 0;
    width: 240px;
    height: 500px;
  }
  .brand-name {
    position: absolute;
    left: 0;
    top: 0;
    width: 1000px;
    height: 500px;
    margin: 0;
    font-family: "Playball", cursive;
    font-weight: 400;
    color: var(--brand-brown);
    line-height: 1;
  }
  .brand-name span {
    position: absolute;
    white-space: nowrap;
  }
  .brand-name .line-one {
    left: 262px;
    top: 95px;
    font-size: 118px;
  }
  .brand-name .line-two {
    left: 430px;
    top: 235px;
    font-size: 150px;
  }
</style>
</head>
<body>
  <main class="canvas">
    <section class="sign-panel" aria-label="Harbor Lane Deli wall sign">
      <svg class="cup-art" viewBox="0 0 240 500" role="img" aria-label="Illustration of a steaming coffee cup on a saucer">
        <defs>
          <linearGradient id="cupTone" x1="0" y1="0" x2="0" y2="1">
            <stop offset="0" stop-color="var(--art-light)" stop-opacity="0.45"/>
            <stop offset="1" stop-color="var(--art-dark)" stop-opacity="0.55"/>
          </linearGradient>
        </defs>
        <rect x="10" y="10" width="220" height="480" rx="36" fill="url(#cupTone)"/>
      </svg>
      <h1 class="brand-name">
        <span class="line-one">Harbor Lane</span>
        <span class="line-two">Deli</span>
      </h1>
    </section>
  </main>
</body>
</html>
```